Vex Pim ORA Need a custom graphic

I need to have the attached chart re-designed in a hand colored pencil format. The heading needs to be changed to "The most effective methods for hiring sales people". Do not include the background logo in the sample file.

Place the attached Vex Pim ORA logo next to the most effective methods (91%)

```html
<!DOCTYPE html>
<html lang="en">
<head>
<meta charset="utf-8">
<title>The Most Effective Methods for Hiring Sales People</title>
<link href="https://fonts.googleapis.com/css2?family=Patrick+Hand&display=swap" rel="stylesheet">
<style>
  :root {
    --backdrop: #d9d9d9;
    --card: #ffffff;
    --navy: #163646;
    --blue: #2a9ad8;
    --ink: #1a1a1a;
    --axis-ink: #1f3a4d;
    --grid: #a8a8a8;
    --red: #c0161f;
    --brand: #1f3b6f;
  }
  html, body {
    margin: 0;
    padding: 0;
    width: 1200px;
    height: 1200px;
    overflow: hidden;
    background: var(--backdrop);
  }
  .chart-canvas { display: block; width: 1200px; height: 1200px; }
  .hand { font-family: "Patrick Hand", cursive; }
  .title-text { fill: #ffffff; font-size: 62px; }
  .tick-label { fill: var(--axis-ink); font-size: 40px; }
  .axis-title { fill: var(--blue); font-size: 54px; }
  .grid-line { stroke: var(--grid); stroke-width: 1.6; }
  .trend-line { fill: none; stroke: var(--red); stroke-width: 5; stroke-linecap: round; stroke-linejoin: round; }
  .data-point { fill: #ffffff; stroke: var(--red); stroke-width: 2.5; }
  .label-shadow { fill: #ffffff; stroke: var(--ink); stroke-width: 1.6; }
  .label-hatch { fill: url(#hatch); }
  .label-box { fill: #ffffff; stroke: var(--ink); stroke-width: 1.8; }
  .label-text { fill: var(--ink); font-size: 28px; }
  .pointer { fill: #fbe7e8; stroke: var(--red); stroke-width: 2; stroke-linejoin: round; }
  .brand-name { fill: var(--brand); font-size: 32px; }
</style>
</head>
<body>
<svg class="chart-canvas" viewBox="0 0 1932 1932" xmlns="http://www.w3.org/2000/svg">
  <defs>
    <pattern id="hatch" width="5" height="5" patternUnits="userSpaceOnUse" patternTransform="rotate(90)">
      <line x1="0" y1="0" x2="0" y2="5" stroke="#1a1a1a" stroke-width="1.6"/>
    </pattern>
    <polygon id="pointer-arrow" class="pointer" points="-58,-7 -22,-7 -22,-15 0,0 -22,15 -22,7 -58,7"/>
  </defs>

  <rect class="card" x="134" y="431" width="1669" height="1080" fill="var(--card)"/>

  <g class="title-band">
    <rect x="286" y="453" width="1327" height="80" fill="var(--navy)"/>
    <rect x="286" y="532" width="1327" height="15" fill="var(--blue)"/>
    <text class="hand title-text" x="938" y="522" text-anchor="middle" textLength="1148" lengthAdjust="spacingAndGlyphs">THE MOST EFFECTIVE METHODS FOR HIRING SALES PEOPLE</text>
  </g>

  <g class="grid">
    <rect x="286" y="547" width="1327" height="840" fill="none" class="grid-line"/>
    <line class="grid-line" x1="286" y1="640" x2="1613" y2="640"/>
    <line class="grid-line" x1="286" y1="733" x2="1613" y2="733"/>
    <line class="grid-line" x1="286" y1="827" x2="1613" y2="827"/>
    <line class="grid-line" x1="286" y1="920" x2="1613" y2="920"/>
    <line class="grid-line" x1="286" y1="1013" x2="1613" y2="1013"/>
    <line class="grid-line" x1="286" y1="1107" x2="1613" y2="1107"/>
    <line class="grid-line" x1="286" y1="1200" x2="1613" y2="1200"/>
    <line class="grid-line" x1="286" y1="1293" x2="1613" y2="1293"/>
    <line class="grid-line" x1="407" y1="547" x2="407" y2="1387"/>
    <line class="grid-line" x1="527" y1="547" x2="527" y2="1387"/>
    <line class="grid-line" x1="648" y1="547" x2="648" y2="1387"/>
    <line class="grid-line" x1="768" y1="547" x2="768" y2="1387"/>
    <line class="grid-line" x1="889" y1="547" x2="889" y2="1387"/>
    <line class="grid-line" x1="1010" y1="547" x2="1010" y2="1387"/>
    <line class="grid-line" x1="1131" y1="547" x2="1131" y2="1387"/>
    <line class="grid-line" x1="1251" y1="547" x2="1251" y2="1387"/>
    <line class="grid-line" x1="1372" y1="547" x2="1372" y2="1387"/>
    <line class="grid-line" x1="1493" y1="547" x2="1493" y2="1387"/>
  </g>

  <g class="y-ticks hand">
    <text class="tick-label" x="274" y="590" text-anchor="end">0.90</text>
    <text class="tick-label" x="274" y="678" text-anchor="end">0.80</text>
    <text class="tick-label" x="274" y="766" text-anchor="end">0.70</text>
    <text class="tick-label" x="274" y="856" text-anchor="end">0.60</text>
    <text class="tick-label" x="274" y="944" text-anchor="end">0.50</text>
    <text class="tick-label" x="274" y="1033" text-anchor="end">0.40</text>
    <text class="tick-label" x="274" y="1120" text-anchor="end">0.30</text>
    <text class="tick-label" x="274" y="1208" text-anchor="end">0.20</text>
    <text class="tick-label" x="274" y="1296" text-anchor="end">0.10</text>
    <text class="tick-label" x="274" y="1388" text-anchor="end">0.00</text>
  </g>

  <text class="hand axis-title" transform="translate(202 972) rotate(-90)" text-anchor="middle" textLength="396" lengthAdjust="spacingAndGlyphs">PREDICTIVE VALIDITY</text>
  <text class="hand axis-title" x="968" y="1465" text-anchor="middle" textLength="302" lengthAdjust="spacingAndGlyphs">HIRING METHOD</text>

  <path class="trend-line" d="M407,1313 C430,1298 445,1282 465,1272 C480,1262 480,1250 512,1228 C560,1214 600,1210 649,1198 L767,1192 C810,1182 850,1172 889,1160 C925,1164 970,1162 1013,1164 C1060,1140 1080,1100 1128,1085 C1160,1050 1200,970 1251,912 C1290,880 1330,865 1372,830 C1420,800 1460,750 1493,710 C1520,665 1540,648 1560,630 C1580,605 1590,585 1613,566"/>

  <g class="data-points">
    <circle class="data-point" cx="407" cy="1313" r="9"/>
    <circle class="data-point" cx="512" cy="1228" r="9"/>
    <circle class="data-point" cx="649" cy="1198" r="9"/>
    <circle class="data-point" cx="767" cy="1192" r="9"/>
    <circle class="data-point" cx="889" cy="1160" r="9"/>
    <circle class="data-point" cx="1013" cy="1164" r="9"/>
    <circle class="data-point" cx="1128" cy="1085" r="9"/>
    <circle class="data-point" cx="1251" cy="912" r="9"/>
    <circle class="data-point" cx="1372" cy="830" r="9"/>
    <circle class="data-point" cx="1493" cy="710" r="9"/>
    <circle class="data-point" cx="1613" cy="566" r="9"/>
  </g>

  <g class="pointers">
    <use href="#pointer-arrow" transform="translate(1585 568) rotate(-25)"/>
    <use href="#pointer-arrow" transform="translate(1470 705) rotate(25)"/>
    <use href="#pointer-arrow" transform="translate(1340 815) rotate(25)"/>
    <use href="#pointer-arrow" transform="translate(1228 910) rotate(-8)"/>
    <use href="#pointer-arrow" transform="translate(1143 1092) rotate(215)"/>
    <use href="#pointer-arrow" transform="translate(1022 1178) rotate(235)"/>
    <use href="#pointer-arrow" transform="translate(772 1208) rotate(230)"/>
    <use href="#pointer-arrow" transform="translate(880 1130) rotate(62)"/>
    <use href="#pointer-arrow" transform="translate(650 1172) rotate(80)"/>
    <use href="#pointer-arrow" transform="translate(508 1218) rotate(58)"/>
    <use href="#pointer-arrow" transform="translate(424 1315) rotate(195)"/>
  </g>

  <g class="labels hand">
    <g class="label">
      <rect class="label-shadow label-hatch" x="993" y="571" width="526" height="45" rx="6"/>
      <rect class="label-box" x="987" y="565" width="526" height="45" rx="6"/>
      <text class="label-text" x="1250" y="597" text-anchor="middle" textLength="500" lengthAdjust="spacingAndGlyphs">SALES-SPECIFIC MULTI-MEASUREMENT ASSESSMENT, 91%</text>
    </g>
    <g class="label">
      <rect class="label-shadow label-hatch" x="1013" y="668" width="393" height="46" rx="6"/>
      <rect class="label-box" x="1007" y="662" width="393" height="46" rx="6"/>
      <text class="label-text" x="1203" y="694" text-anchor="middle" textLength="364" lengthAdjust="spacingAndGlyphs">MULTI-MEASUREMENT ASSESSMENT, 71%</text>
    </g>
    <g class="label">
      <rect class="label-shadow label-hatch" x="748" y="775" width="526" height="46" rx="6"/>
      <rect class="label-box" x="742" y="769" width="526" height="46" rx="6"/>
      <text class="label-text" x="1003" y="801" text-anchor="middle" textLength="476" lengthAdjust="spacingAndGlyphs">HIGHLY STRUCTURED INTERVIEW WITH SCORECARD,57%</text>
    </g>
    <g class="label">
      <rect class="label-shadow label-hatch" x="862" y="891" width="308" height="45" rx="6"/>
      <rect class="label-box" x="856" y="885" width="308" height="45" rx="6"/>
      <text class="label-text" x="1007" y="917" text-anchor="middle" textLength="270" lengthAdjust="spacingAndGlyphs">GENERAL MENTAL ABILITY, 51%</text>
    </g>
    <g class="label">
      <rect class="label-shadow label-hatch" x="741" y="1004" width="223" height="47" rx="6"/>
      <rect class="label-box" x="735" y="998" width="223" height="47" rx="6"/>
      <text class="label-text" x="846" y="1031" text-anchor="middle" textLength="204" lengthAdjust="spacingAndGlyphs">REFERENCE CHECK, 23%</text>
    </g>
    <g class="label">
      <rect class="label-shadow label-hatch" x="446" y="1063" width="345" height="47" rx="6"/>
      <rect class="label-box" x="440" y="1057" width="345" height="47" rx="6"/>
      <text class="label-text" x="611" y="1090" text-anchor="middle" textLength="310" lengthAdjust="spacingAndGlyphs">BEHAVIOR/PERSONALITY TEST, 20%</text>
    </g>
    <g class="label">
      <rect class="label-shadow label-hatch" x="345" y="1123" width="143" height="46" rx="6"/>
      <rect class="label-box" x="339" y="1117" width="143" height="46" rx="6"/>
      <text class="label-text" x="408" y="1149" text-anchor="middle" textLength="111" lengthAdjust="spacingAndGlyphs">RESUME, 18%</text>
    </g>
    <g class="label">
      <rect class="label-shadow label-hatch" x="665" y="1266" width="295" height="45" rx="6"/>
      <rect class="label-box" x="659" y="1260" width="295" height="45" rx="6"/>
      <text class="label-text" x="807" y="1292" text-anchor="middle" textLength="258" lengthAdjust="spacingAndGlyphs">TRADITIONAL INTERVIEW, 20%</text>
    </g>
    <g class="label">
      <rect class="label-shadow label-hatch" x="1025" y="1233" width="296" height="47" rx="6"/>
      <rect class="label-box" x="1019" y="1227" width="296" height="47" rx="6"/>
      <text class="label-text" x="1167" y="1260" text-anchor="middle" textLength="274" lengthAdjust="spacingAndGlyphs">EMOTIONAL INTELLIGENCE, 23%</text>
    </g>
    <g class="label">
      <rect class="label-shadow label-hatch" x="1187" y="1133" width="197" height="47" rx="6"/>
      <rect class="label-box" x="1181" y="1127" width="197" height="47" rx="6"/>
      <text class="label-text" x="1279" y="1160" text-anchor="middle" textLength="157" lengthAdjust="spacingAndGlyphs">SKILLS TEST, 33%</text>
    </g>
    <g class="label">
      <rect class="label-shadow label-hatch" x="480" y="1343" width="198" height="45" rx="6"/>
      <rect class="label-box" x="474" y="1337" width="198" height="45" rx="6"/>
      <text class="label-text" x="572" y="1369" text-anchor="middle" textLength="162" lengthAdjust="spacingAndGlyphs">CULTURE TEST, 13%</text>
    </g>
  </g>

  <text class="hand brand-name" x="1632" y="578" textLength="160" lengthAdjust="spacingAndGlyphs">Vex Pim ORA</text>
</svg>
</body>
</html>
```